Business Card Design Project

Financial planning, Insurance and Real estate - Financial Services company

Contact Information for Business Card

Looking for something simple in design -
Tolverin Equity LLC
Tolverin Wealth Managment

```html
<!DOCTYPE html>
<html lang="en">
<head>
<meta charset="utf-8">
<title>Tolverin Wealth Management – Business Card</title>
<link rel="stylesheet" href="https://fonts.googleapis.com/css2?family=Lato:ital,wght@0,400;0,700;1,700&family=Roboto+Condensed:wght@700&display=swap">
<style>
  :root {
    --page-bg: #ececec;
    --card-bg: #ffffff;
    --brand-blue: #0a7fc0;
    --ink: #111111;
    --ink-soft: #2b2b2b;
    --rule: #222222;
  }
  * { margin: 0; padding: 0; box-sizing: border-box; }
  html, body {
    width: 1200px;
    height: 985px;
    overflow: hidden;
    background: var(--page-bg);
    font-family: "Lato", Arial, sans-serif;
  }
  .card {
    position: absolute;
    left: 75px;
    top: 177px;
    width: 1050px;
    height: 630px;
    background: var(--card-bg);
  }
  .brand-name {
    position: absolute;
    left: 70px;
    top: 276px;
    font-family: "Roboto Condensed", "Arial Narrow", sans-serif;
    font-weight: 700;
    font-size: 20px;
    color: var(--brand-blue);
    line-height: 1;
  }
  .holder {
    position: absolute;
    right: 67px;
    top: 94px;
    text-align: right;
  }
  .holder-name {
    font-size: 28px;
    font-weight: 400;
    color: var(--brand-blue);
    line-height: 1.1;
  }
  .holder-name strong { font-weight: 700; }
  .holder-title {
    margin-top: 4px;
    font-size: 20px;
    font-weight: 700;
    font-style: italic;
    color: var(--ink);
    line-height: 1.1;
  }
  .divider {
    position: absolute;
    left: 62px;
    top: 428px;
    width: 921px;
    height: 3px;
    background: var(--rule);
  }
  .contact-list {
    position: absolute;
    left: 70px;
    top: 452px;
    list-style: none;
  }
  .contact-item {
    display: flex;
    align-items: center;
    height: 43px;
    font-size: 22px;
    color: var(--ink-soft);
  }
  .contact-icon {
    width: 22px;
    height: 22px;
    margin-right: 14px;
    fill: var(--brand-blue);
  }
  .web-address {
    position: absolute;
    right: 67px;
    top: 497px;
    text-align: right;
    line-height: 1.55;
  }
  .website { font-size: 23px; font-weight: 700; color: var(--ink); }
  .street { font-size: 22px; font-weight: 700; color: var(--brand-blue); }
  .footer-band {
    position: absolute;
    left: 0;
    bottom: 0;
    width: 100%;
    height: 25px;
    background: var(--brand-blue);
  }
</style>
</head>
<body>
  <div class="card">
    <div class="brand-name">Tolverin Wealth Management</div>

    <div class="holder">
      <div class="holder-name">Corinne <strong>Adler</strong></div>
      <div class="holder-title">Office Manager</div>
    </div>

    <div class="divider"></div>

    <ul class="contact-list">
      <li class="contact-item">
        <svg class="contact-icon" viewBox="0 0 24 24" aria-hidden="true">
          <path d="M3 9c0-3 4-5 9-5s9 2 9 5v2h-5V9c-1-.6-2.5-1-4-1s-3 .4-4 1v2H3z"/>
          <path d="M6 12h12l2 8H4z"/>
        </svg>
        555.014.2910
      </li>
      <li class="contact-item">
        <svg class="contact-icon" viewBox="0 0 24 24" aria-hidden="true">
          <rect x="6" y="2" width="12" height="6"/>
          <path d="M2 9h20v9h-4v-4H6v4H2z"/>
          <rect x="7" y="15" width="10" height="7"/>
        </svg>
        555.014.2971
      </li>
      <li class="contact-item">
        <svg class="contact-icon" viewBox="0 0 24 24" aria-hidden="true">
          <path d="M2 5h20v2l-10 6L2 7z"/>
          <path d="M2 9l10 6 10-6v10H2z"/>
        </svg>
        cadler@tolverinwm.com
      </li>
    </ul>

    <div class="web-address">
      <div class="website">www.tolverinwealthm.com</div>
      <div class="street">2817 W Larkspur Ave Fairhaven Indiana 46000</div>
    </div>

    <div class="footer-band"></div>
  </div>
</body>
</html>
```